Business card for utility of the future

I need a business card template designed for brookvane. We provide sustainable water, energy and waste services to homes.

The card should include name, position, email address, phone number, website and our logo (attached). I would like it to convey professionalism and creativity.

Target Market(s)

Homeowners, investors, corporate partners.

Industry/Entity Type

Utility

Contact Information for Business Card

The card should include name, position, email address, phone number, website and our logo (attached).

```html
<!DOCTYPE html>
<html lang="en">
<head>
<meta charset="utf-8">
<title>brookvane business card</title>
<link rel="stylesheet" href="https://fonts.googleapis.com/css2?family=Open+Sans:wght@400;600;700;800&display=swap">
<style>
  :root {
    --bg: #2b2d30;
    --green: #66b677;
    --green-deep: #5aa96b;
    --orange: #e9785a;
    --ink: #3a3a3a;
    --muted: #555;
    --white: #ffffff;
  }
  * { margin: 0; padding: 0; box-sizing: border-box; }
  html, body { width: 1200px; height: 900px; overflow: hidden; }
  body {
    background: var(--bg);
    font-family: "Open Sans", Arial, sans-serif;
    position: relative;
  }
  .card {
    position: absolute;
    width: 520px;
    height: 300px;
    border-radius: 26px;
    overflow: hidden;
    top: 300px;
  }
  .card-front { left: 50px; background: var(--white); }
  .card-back { left: 630px; background: var(--green); }

  .front-swoosh { position: absolute; inset: 0; }

  .person { position: absolute; left: 118px; top: 118px; }
  .person-name {
    font-size: 25px; font-weight: 700; letter-spacing: 1px;
    color: var(--ink); text-transform: uppercase; line-height: 1;
  }
  .person-name .surname { color: var(--orange); }
  .person-role {
    margin-top: 8px; font-size: 14px; font-weight: 400;
    letter-spacing: 0.5px; color: var(--muted); text-transform: uppercase;
  }

  .contact {
    position: absolute; left: 222px; top: 192px;
    padding-left: 16px; border-left: 1.5px solid var(--green);
    list-style: none;
  }
  .contact li {
    display: flex; align-items: center; gap: 9px;
    font-size: 13px; color: var(--muted); height: 23px;
  }
  .contact svg { width: 13px; height: 13px; fill: var(--green); flex: none; }
  .contact .web-accent { color: var(--green); }

  .brand-front {
    position: absolute; right: 34px; top: 70px;
    font-size: 50px; font-weight: 800; color: var(--green);
    letter-spacing: -1.5px; line-height: 1;
  }

  .back-frame {
    position: absolute; inset: 22px;
    border: 1px solid rgba(255,255,255,0.85); border-radius: 4px;
  }
  .brand-back {
    position: absolute; inset: 0;
    display: flex; align-items: center; justify-content: center;
    font-size: 62px; font-weight: 800; color: var(--white);
    letter-spacing: -2px;
  }
</style>
</head>
<body>
  <section class="card card-front">
    <svg class="front-swoosh" viewBox="0 0 520 300" width="520" height="300" aria-hidden="true">
      <path d="M0 0 H180 C110 40 40 130 0 265 Z" fill="var(--green)"/>
      <path d="M0 0 H105 C65 25 25 70 0 125 L0 108 C22 62 55 22 88 0 Z" fill="var(--orange)"/>
      <path d="M0 0 H88 C55 22 22 62 0 108 Z" fill="var(--green-deep)"/>
    </svg>

    <div class="brand-front">brookvane</div>

    <div class="person">
      <p class="person-name">Mara <span class="surname">Ellison</span></p>
      <p class="person-role">CEO/Founder</p>
    </div>

    <ul class="contact">
      <li>
        <svg viewBox="0 0 24 24"><path d="M6.6 10.8a15.1 15.1 0 0 0 6.6 6.6l2.2-2.2c.3-.3.7-.4 1-.2 1.1.4 2.3.6 3.6.6.6 0 1 .4 1 1V20c0 .6-.4 1-1 1A17 17 0 0 1 3 4c0-.6.4-1 1-1h3.5c.6 0 1 .4 1 1 0 1.3.2 2.5.6 3.6.1.3 0 .7-.2 1z"/></svg>
        <span>+61740005218</span>
      </li>
      <li>
        <svg viewBox="0 0 24 24"><path d="M2 5h20v14H2z M4 7v.4l8 5.2 8-5.2V7z" fill-rule="evenodd"/></svg>
        <span>marae@brookvane.com</span>
      </li>
      <li>
        <svg viewBox="0 0 24 24"><circle cx="12" cy="12" r="10"/><path d="M2 12h20M12 2c3 3 3 17 0 20M12 2c-3 3-3 17 0 20" stroke="#fff" stroke-width="1.4" fill="none"/></svg>
        <span>www.<span class="web-accent">yourwebsite</span>.com</span>
      </li>
    </ul>
  </section>

  <section class="card card-back">
    <div class="back-frame"></div>
    <div class="brand-back">brookvane</div>
  </section>
</body>
</html>
```